The Copper Fellow Mo Wax Label

Hi Chaps,

We are needing a lable for our new moustache wax.

The design needs to be on a circular label. the size of the label is 32mm in diameter.

It needs to align with our branding from our beard oil product. checkout www.thecopperfellow-demo.com to get an insight of this.

what needs to be on the label:

- The copper fellow logo (please pull from website, will send through hi def image when design is selected)
- Fine Grain Moustache Wax
- the word "soft/medium hold"

This project will be open for 48 hours.

Any questions, please ask asap.
Updates

Our Logo and fonts that we use for our brand are now attached to the brief. 

Industry/Entity Type

Product

Requirements
Must have
• Must have
The copper fellow logo (please pull from website, will send through hi def image when design is selected)
- Fine Grain Moustache Wax
- allign with branding
- actual size 32mm diameter

```html
<!DOCTYPE html>
<html lang="en">
<head>
<meta charset="utf-8">
<title>The Copper Fellow – Fine Grain Moustache Wax Labels</title>
<link rel="stylesheet" href="https://fonts.googleapis.com/css2?family=Archivo+Black&family=Archivo:wght@400;700&family=Pinyon+Script&display=swap">
<style>
  :root {
    --page-bg: #e5e5e5;
    --edge: #1d1d1d;
    --sky-bg: #9be6f4;
    --sky-band: #6cc0cf;
    --sky-ink: #0d4a5c;
    --sky-dot: #4a7f8a;
    --sky-orn: #86d2e0;
    --paper-bg: #ffffff;
    --paper-band: #d4d4d4;
    --paper-ink: #141414;
    --paper-dot: #555555;
    --paper-orn: #e6e6e6;
    --sand-bg: #e3d7b4;
    --sand-band: #b19b84;
    --sand-ink: #8a4a36;
    --sand-accent: #b4520f;
    --sand-dot: #a07c50;
    --sand-orn: #d6c8a2;
  }
  html, body {
    margin: 0;
    padding: 0;
    width: 1200px;
    height: 844px;
    overflow: hidden;
    background: var(--page-bg);
  }
  .canvas { display: block; width: 1200px; height: 844px; }

  .label--sky   { --bg: var(--sky-bg);   --band: var(--sky-band);   --ink: var(--sky-ink);   --accent: var(--sky-ink);     --dot: var(--sky-dot);   --orn: var(--sky-orn); }
  .label--paper { --bg: var(--paper-bg); --band: var(--paper-band); --ink: var(--paper-ink); --accent: var(--paper-ink);   --dot: var(--paper-dot); --orn: var(--paper-orn); }
  .label--sand  { --bg: var(--sand-bg);  --band: var(--sand-band);  --ink: var(--sand-ink);  --accent: var(--sand-accent); --dot: var(--sand-dot);  --orn: var(--sand-orn); }

  .label__disc { fill: var(--bg); stroke: var(--edge); stroke-width: 2; }
  .label__dots { fill: none; stroke: var(--dot); stroke-width: 2.4; stroke-linecap: round; stroke-dasharray: 0.1 6.2; }
  .label__band { fill: var(--band); }
  .label__ornament { fill: var(--orn); }
  .label__ornament--small { fill: var(--dot); }
  .label__badge { fill: var(--bg); stroke: var(--ink); stroke-width: 2.5; }
  .label__brand {
    font-family: "Archivo", sans-serif; font-weight: 700; font-size: 14px;
    fill: var(--ink); text-anchor: middle; letter-spacing: 0.3px;
  }
  .label__band-word {
    font-family: "Archivo Black", sans-serif; font-size: 21px; fill: var(--ink);
  }
  .label__kicker {
    font-family: "Archivo", sans-serif; font-weight: 400; font-size: 12px;
    fill: var(--ink); text-anchor: middle; letter-spacing: 0.5px;
  }
  .label__rule { stroke: var(--ink); stroke-width: 1; }
  .label__product {
    font-family: "Archivo", sans-serif; font-weight: 700; font-size: 19px;
    fill: var(--accent); text-anchor: middle;
  }
  .label__hold {
    font-family: "Pinyon Script", cursive; font-size: 16px;
    fill: var(--ink); text-anchor: middle;
  }
</style>
</head>
<body>
<svg class="canvas" viewBox="0 0 1200 844" xmlns="http://www.w3.org/2000/svg">
  <defs>
    <clipPath id="disc-clip">
      <circle cx="0" cy="0" r="154"/>
    </clipPath>
    <g id="label-body">
      <circle class="label__disc" r="155"/>
      <circle class="label__dots" r="145"/>
      <g role="img" aria-label="Decorative flourish swirls">
        <ellipse class="label__ornament" cx="-92" cy="-72" rx="28" ry="20"/>
        <ellipse class="label__ornament" cx="92" cy="-72" rx="28" ry="20"/>
      </g>
      <g role="img" aria-label="Small ornament">
        <ellipse class="label__ornament--small" cx="0" cy="-134" rx="8" ry="3"/>
        <ellipse class="label__ornament--small" cx="0" cy="136" rx="8" ry="3"/>
      </g>
      <rect class="label__band" x="-155" y="-21" width="310" height="37" clip-path="url(#disc-clip)"/>
      <text class="label__band-word" x="-64" y="5" text-anchor="end">FINE</text>
      <text class="label__band-word" x="64" y="5" text-anchor="start">GRAIN</text>
      <circle class="label__badge" cx="0" cy="-26" r="56"/>
      <text class="label__brand" x="0" y="-30">The Copper</text>
      <text class="label__brand" x="0" y="-12">Fellow</text>
      <line class="label__rule" x1="-76" y1="66" x2="-40" y2="66"/>
      <line class="label__rule" x1="40" y1="66" x2="76" y2="66"/>
      <text class="label__kicker" x="0" y="70">FINE GRAIN</text>
      <text class="label__product" x="0" y="92">MOUSTACHE WAX</text>
      <text class="label__hold" x="0" y="112">soft/medium hold</text>
    </g>
  </defs>

  <g class="label label--sky" transform="translate(258 408)">
    <use href="#label-body"/>
  </g>
  <g class="label label--paper" transform="translate(599 408)">
    <use href="#label-body"/>
  </g>
  <g class="label label--sand" transform="translate(954 408)">
    <use href="#label-body"/>
  </g>
</svg>
</body>
</html>
```